Ecommerce Website

Hello designers of Pixel Harbor,

Today I'm requesting webpage designs for my new start up business in Toronto Canada. I have little or no experience in this field so I decided to outsource it here! My business revolves around the retail of customizable smartphone cases, as well as other objects such as mouse pads, mugs, etc.. Our main focus is smartphone cases, tablets and such. There are a few of these types of websites out already so the idea shouldn't be too foreign. I am looking for a minimalist look for my website revolving around light colours. Should convey a sense of simplistic design with elegant feel while including aspects of the business. Please see current website at brindlecove.ca to see how the set-up is (currently on pre-made template). Should have a similar feel to it. Also i have a post for logo design as i currently do not have one. If you can create a logo as well for my other post along with this one, gives preference to artist.

http://jobs.pixelharbor.com/job.aspx?id=587216
Updates

The design should be transferable to the other webpages on the site. The overall look should be the same (borders, buttons, etc)

I am not sure if I'm allowed to request the page in coding as it said non-coded earlier. However it would be preferable to have the website in CSS or HTML as well as a PSD version for alterations.

Wasn't too clear about the total requirements. We are looking for a main homepage as well as a general design for the rest of our pages such as browsing catalogue page, product page, etc.. Should be a general look that can be used for multiple pages.

I have committed the payment so please do not hesitate to post designs.

To All designers.  I have attached the logo to the brief. It has multiple colors which you can choose from. The last one on the second row is the one i prefer the best however if your site can match well with any other ones, that is okay as well. 

Reason: have a few designs for selection in mind however need to get it to the final point.

Target Market(s)

Young adults ages 19 - 32

Industry/Entity Type

Retail

Requirements
Must have
• Main slider design - Main page will have a slider which displays new products or services. Please see brindlecove.ca for example

Note worthy - Currently we are using a service from http://www.vantoriq.com/ so please make sure that it the design will work with that in mind.

```html
<!DOCTYPE html>
<html lang="en">
<head>
<meta charset="utf-8">
<title>Brindlecove – Home</title>
<link rel="stylesheet" href="https://fonts.googleapis.com/css2?family=Arimo:wght@400;700&family=Lora:wght@400&family=Oswald:wght@500&family=Russo+One&family=Noto+Sans&family=Codystar&display=swap">
<style>
:root{
  --orange:#ff9a1f;
  --orange-deep:#f07c00;
  --orange-light:#ffa63a;
  --black:#050505;
  --dark:#3a3a3a;
  --footer:#3c3c3c;
  --grey-bg:#efefef;
  --grey-line:#d9d9d9;
  --text:#222;
  --muted:#777;
  --price:#d81b12;
  --white:#fff;
  --star:#f8b526;
  --star-off:#dadada;
}
*{margin:0;padding:0;box-sizing:border-box}
html,body{width:890px;height:1200px;overflow:hidden}
body{position:relative;background:var(--white);font-family:Arimo,Arial,sans-serif;color:var(--text)}
.abs{position:absolute}
a{color:inherit;text-decoration:none}

.top-bar{left:0;top:0;width:890px;height:29px;background:repeating-linear-gradient(135deg,#4a4a4a 0 2px,#3d3d3d 2px 4px)}
.top-links{right:110px;top:8px;font-size:10px;color:#eee;word-spacing:2px}
.header{left:0;top:29px;width:890px;height:79px;background:var(--black)}
.brand{left:94px;top:20px;font-family:Lora,Georgia,serif;font-size:29px;color:var(--white);letter-spacing:.3px}
.welcome{right:124px;top:16px;font-size:8.5px;color:var(--white)}
.cart-line{right:178px;top:40px;font-size:7.5px;color:var(--white);white-space:nowrap}
.cart-line em{font-style:normal;color:var(--orange)}
.cart-btn{left:724px;top:35px;width:42px;height:18px;background:var(--orange);border:1px solid #ffc27a;border-radius:2px;color:var(--white);font-size:7.5px;text-align:center;line-height:16px}
.stripe-band{left:0;top:108px;width:890px;height:56px;background:repeating-linear-gradient(135deg,#cfcfcf 0 2px,#e3e3e3 2px 4px)}
.nav{left:78px;top:112px;width:730px;height:58px;background:var(--orange)}
.nav ul{list-style:none;position:absolute;left:32px;top:17px;display:flex;gap:27px;font-family:Oswald,sans-serif;font-size:15.5px;color:var(--white)}
.tel{left:546px;top:8px;font-size:9px;font-style:italic;color:var(--white);word-spacing:2px;white-space:nowrap}
.search{left:543px;top:25px;width:143px;height:23px;background:var(--white);border:1px solid #ffd39c;font-size:7.5px;font-style:italic;color:#aaa;padding:7px 8px}
.search-btn{left:690px;top:25px;width:23px;height:23px;background:#f26d1f;border:1px solid #ffb070;border-radius:3px}
.nav-shadow{left:110px;top:170px;width:670px;height:8px;background:radial-gradient(ellipse at top,rgba(0,0,0,.35),transparent 70%)}

.slider{left:0;top:164px;width:890px;height:288px}
.slide-photo{left:192px;top:36px;width:258px;height:212px;background:linear-gradient(160deg,#f4f6f8 0%,#3a2c2e 40%,#1d1517 75%,#f2f3f5 100%);border-radius:6px}
.slide-title{right:160px;top:52px;white-space:nowrap;text-align:right;font-family:Codystar,cursive;font-size:24px;color:var(--orange-deep);font-weight:700}
.slide-sub{right:160px;top:100px;font-family:"Russo One",sans-serif;font-size:20px;color:#111}
.slide-text{right:157px;top:130px;width:240px;text-align:right;font-family:"Noto Sans",sans-serif;font-size:12.4px;line-height:14px;color:#333}
.slide-btn{left:616px;top:190px;width:116px;height:34px;background:var(--orange-deep);border-radius:3px;color:var(--white);font-family:"Russo One",sans-serif;font-size:11.5px;text-align:center;line-height:34px;box-shadow:0 2px 3px rgba(0,0,0,.15)}
.arrow{top:118px}

.action-band{left:0;top:452px;width:890px;height:64px;background:var(--orange-light)}
.choose{left:116px;top:27px;font-family:"Russo One",sans-serif;font-size:11.5px;color:var(--white);white-space:nowrap}
.select{left:270px;top:22px;width:140px;height:24px;background:var(--white);border:1px solid #ddd;font-size:8px;font-style:italic;color:#444;padding:7px 11px}
.select svg{position:absolute;right:8px;top:9px}
.go{left:414px;top:22px;width:54px;height:24px;background:#222;border-radius:3px;color:var(--white);font-size:10px;letter-spacing:1px;text-align:center;line-height:25px}
.login{left:484px;top:4px;width:126px;height:60px;background:var(--orange-deep)}
.login span,.register span{position:absolute;top:24px;font-family:"Russo One",sans-serif;font-size:12px;color:var(--white);letter-spacing:1px;white-space:nowrap}
.register{left:610px;top:4px;width:280px;height:60px}

.features{left:112px;top:524px;width:680px;height:108px}
.feature{position:absolute;top:0;width:220px}
.feature-icon{position:absolute;left:0;top:0;width:28px;height:28px;border-radius:4px}
.feature h3{position:absolute;left:44px;top:22px;font-size:11.3px;font-weight:400;white-space:nowrap}
.feature p{position:absolute;left:3px;top:49px;width:210px;font-size:8.2px;line-height:14px;color:var(--muted)}

.products{left:107px;top:634px;width:667px;height:282px;background:var(--grey-bg);border:1px solid #e2e2e2;border-radius:3px}
.card{position:absolute;top:11px;width:152px;height:255px;background:var(--white);border:1px solid var(--grey-line)}
.card-img{position:absolute;left:5px;top:5px;width:140px;height:147px;border:1px solid #eee}
.card-img i{position:absolute;left:30px;top:12px;width:80px;height:122px;border-radius:8px}
.card-name{position:absolute;left:0;top:160px;width:150px;text-align:center;font-size:10px}
.card-price{position:absolute;left:9px;top:181px;font-size:12px;color:var(--price)}
.card-add{position:absolute;left:75px;top:175px;width:67px;height:19px;background:var(--orange-deep);border:1px solid #ffb36a;border-radius:2px;color:var(--white);font-size:7.2px;text-align:center;line-height:17px}
.card-foot{position:absolute;left:0;top:207px;width:150px;height:46px;background:#f3f3f3;border-top:1px solid #e6e6e6}
.stars{position:absolute;left:37px;top:7px;display:flex;gap:2px}
.card-links{position:absolute;left:7px;top:28px;font-size:7.3px;color:#888;white-space:nowrap}
.side-tab{top:109px;width:22px;height:48px;background:var(--orange);border-radius:2px;box-shadow:0 2px 2px rgba(0,0,0,.2)}

.brands{left:107px;top:932px;width:667px;height:42px;background:#f3f3f3;border:1px solid #e0e0e0;border-radius:3px}
.brand-name{position:absolute;top:13px;font-size:15px;font-weight:700;color:#3b3b3b;letter-spacing:.5px;white-space:nowrap}

.footer{left:0;top:984px;width:890px;height:216px;background:var(--footer)}
.footer h4{position:absolute;top:17px;font-size:13px;font-weight:400;color:var(--white)}
.f-text{position:absolute;font-size:8.3px;line-height:14px;color:var(--white)}
.f-icon{position:absolute;width:21px;height:21px;border-radius:50%;background:#f36f21}
.f-list{position:absolute;list-style:none;font-size:8.3px;color:var(--white)}
.f-list li{height:18px}
.f-list li::before{content:"›";margin-right:9px;font-size:11px}
.news-input{left:618px;top:42px;width:160px;height:23px;background:var(--white);border:1px solid #ccc;font-size:7.7px;color:#aaa;padding:7px 8px}
.news-btn{left:787px;top:42px;width:35px;height:22px;background:var(--orange-deep);border-radius:4px;color:var(--white);font-size:8.5px;text-align:center;line-height:22px}
.badge{position:absolute;background:#d8d8d8;border-radius:2px}
.social{position:absolute;top:184px;display:flex;align-items:center;gap:4px;font-size:8.5px;color:var(--white)}
.social b{display:block;width:12px;height:12px;background:#7a9fbd;border-radius:2px}
.copy{left:681px;top:184px;font-size:8.5px;color:var(--white)}
</style>
</head>
<body>
<svg width="0" height="0" style="position:absolute">
  <defs>
    <symbol id="star" viewBox="0 0 20 20"><path d="M10 1l2.7 6 6.3.6-4.8 4.3 1.4 6.4L10 15l-5.6 3.3 1.4-6.4L1 7.6 7.3 7z"/></symbol>
    <symbol id="chev-l" viewBox="0 0 20 30"><path d="M15 3L4 15l11 12" fill="none" stroke="currentColor" stroke-width="4"/></symbol>
    <symbol id="chev-r" viewBox="0 0 20 30"><path d="M5 3l11 12L5 27" fill="none" stroke="currentColor" stroke-width="4"/></symbol>
  </defs>
</svg>

<div class="abs top-bar"><div class="abs top-links">My Account &nbsp;| &nbsp;My Wishlist &nbsp;| &nbsp;Checkout &nbsp;| &nbsp;Log In</div></div>

<header class="abs header">
  <div class="abs brand">Brindlecove</div>
  <div class="abs welcome">Default welcome msg!</div>
  <div class="abs cart-line">There are <em>items</em> in your cart. <em>$0.00</em></div>
  <div class="abs cart-btn">CART</div>
</header>

<div class="abs stripe-band"></div>
<nav class="abs nav">
  <ul><li>HOME</li><li>DESIGNS</li><li>CREATE</li><li>ABOUT</li><li>CONTACT</li><li>REQUEST A QUOTE</li></ul>
  <div class="abs tel">TEL: &nbsp;(055) 27-41-306 &nbsp;(055) 27-41-306</div>
  <div class="abs search">serch entire store here...</div>
  <div class="abs search-btn"><svg width="21" height="21" viewBox="0 0 21 21"><circle cx="9" cy="9" r="4.5" fill="none" stroke="#fff" stroke-width="2"/><path d="M12.3 12.3l4 4" stroke="#fff" stroke-width="2.2"/></svg></div>
</nav>
<div class="abs nav-shadow"></div>

<section class="abs slider">
  <div class="abs slide-photo" role="img" aria-label="Black ribbed phone case with belt clip holster"></div>
  <svg class="abs arrow" style="left:112px" width="20" height="30" color="#bbb"><use href="#chev-l"/></svg>
  <svg class="abs arrow" style="left:754px" width="20" height="30" color="#bbb"><use href="#chev-r"/></svg>
  <div class="abs slide-title">Orbi Phone Case</div>
  <div class="abs slide-sub">JUST FOR SAFE</div>
  <p class="abs slide-text">Excepteur sint occaecat cupidatat non proident, sunt in culpa qui officia deserunt mollit anim</p>
  <div class="abs slide-btn">GET START NOW</div>
</section>

<section class="abs action-band">
  <div class="abs choose">CHOOSE YOUR DESIGNS</div>
  <div class="abs select">Animals<svg width="9" height="6"><path d="M0 0h9L4.5 6z" fill="#111"/></svg></div>
  <div class="abs go">GO</div>
  <div class="abs login">
    <svg class="abs" style="left:24px;top:12px" width="26" height="32" viewBox="0 0 26 32"><path d="M7 14V9a6 6 0 0112 0v5" fill="none" stroke="#ddd" stroke-width="3"/><rect x="3" y="14" width="20" height="16" rx="2" fill="#bbb"/></svg>
    <span style="left:60px">LOGIN</span>
  </div>
  <div class="abs register">
    <div class="abs" style="left:22px;top:16px;width:26px;height:30px;background:#ffe2b5;border-radius:3px" role="img" aria-label="Notepad and pencil icon"></div>
    <span style="left:62px">REGISTER</span>
  </div>
</section>

<section class="abs features">
  <div class="feature" style="left:0">
    <div class="feature-icon" style="top:16px;background:#8cc63f" role="img" aria-label="Free shipping sticker"></div>
    <h3>FREE WORLDWIDE SHIPPING</h3>
    <p>There are many variations of passages of Lorem Ipsum available, but the majority have suffered alteration in some form, by injected humour, or randomised words which don't look even slightly believable.</p>
  </div>
  <div class="feature" style="left:232px">
    <div class="feature-icon" style="left:3px;top:10px;width:24px;height:34px;background:#e03a1e" role="img" aria-label="Warranty ribbon"></div>
    <h3 style="left:40px">12 MONTHS WARRANTY</h3>
    <p>There are many variations of passages of Lorem Ipsum available, but the majority have suffered alteration in some form, by injected humour, or randomised words which don't look even slightly believable.</p>
  </div>
  <div class="feature" style="left:460px">
    <div class="feature-icon" style="left:1px;top:2px;width:30px;height:40px;background:#e2a65c" role="img" aria-label="Customer service representative illustration"></div>
    <h3>TESTIMONIALS</h3>
    <p>There are many variations of passages of Lorem Ipsum available, but the majority have suffered alteration in some form, by injected humour, or randomised words which don't look even slightly believable.</p>
  </div>
</section>

<section class="abs products">
  <div class="card" style="left:13px">
    <div class="card-img"><i role="img" aria-label="Phone in blue flip case" style="background:linear-gradient(150deg,#2c6fcf,#1a3f8f)"></i></div>
    <div class="card-name">DEMO ITEM</div><div class="card-price">$7678.64</div><div class="card-add">ADD TO CART</div>
    <div class="card-foot"><div class="stars"><svg width="13" height="13" fill="var(--star)"><use href="#star"/></svg><svg width="13" height="13" fill="var(--star)"><use href="#star"/></svg><svg width="13" height="13" fill="var(--star)"><use href="#star"/></svg><svg width="13" height="13" fill="var(--star-off)"><use href="#star"/></svg><svg width="13" height="13" fill="var(--star-off)"><use href="#star"/></svg></div><div class="card-links">+ Add to Wishlist &nbsp;+ Add to Compare</div></div>
  </div>
  <div class="card" style="left:177px">
    <div class="card-img"><i role="img" aria-label="Black grid textured phone cases" style="left:12px;width:116px;background:linear-gradient(90deg,#222 0 70%,#f2f2f2 70%)"></i></div>
    <div class="card-name">DEMO ITEM</div><div class="card-price">$7678.64</div><div class="card-add">ADD TO CART</div>
    <div class="card-foot"><div class="stars"><svg width="13" height="13" fill="var(--star)"><use href="#star"/></svg><svg width="13" height="13" fill="var(--star)"><use href="#star"/></svg><svg width="13" height="13" fill="var(--star)"><use href="#star"/></svg><svg width="13" height="13" fill="var(--star-off)"><use href="#star"/></svg><svg width="13" height="13" fill="var(--star-off)"><use href="#star"/></svg></div><div class="card-links">+ Add to Wishlist &nbsp;+ Add to Compare</div></div>
  </div>
  <div class="card" style="left:340px">
    <div class="card-img"><i role="img" aria-label="Phone in dark slim case" style="left:22px;width:96px;background:linear-gradient(160deg,#3e4a4c,#111)"></i></div>
    <div class="card-name">DEMO ITEM</div><div class="card-price">$7678.64</div><div class="card-add">ADD TO CART</div>
    <div class="card-foot"><div class="stars"><svg width="13" height="13" fill="var(--star)"><use href="#star"/></svg><svg width="13" height="13" fill="var(--star)"><use href="#star"/></svg><svg width="13" height="13" fill="var(--star)"><use href="#star"/></svg><svg width="13" height="13" fill="var(--star-off)"><use href="#star"/></svg><svg width="13" height="13" fill="var(--star-off)"><use href="#star"/></svg></div><div class="card-links">+ Add to Wishlist &nbsp;+ Add to Compare</div></div>
  </div>
  <div class="card" style="left:503px">
    <div class="card-img"><i role="img" aria-label="Phone in lime green case" style="left:45px;width:58px;background:linear-gradient(90deg,#555 0 12%,#b8bf2c 12% 88%,#555 88%)"></i></div>
    <div class="card-name">DEMO ITEM</div><div class="card-price">$7678.64</div><div class="card-add">ADD TO CART</div>
    <div class="card-foot"><div class="stars"><svg width="13" height="13" fill="var(--star)"><use href="#star"/></svg><svg width="13" height="13" fill="var(--star)"><use href="#star"/></svg><svg width="13" height="13" fill="var(--star)"><use href="#star"/></svg><svg width="13" height="13" fill="var(--star-off)"><use href="#star"/></svg><svg width="13" height="13" fill="var(--star-off)"><use href="#star"/></svg></div><div class="card-links">+ Add to Wishlist &nbsp;+ Add to Compare</div></div>
  </div>
  <div class="abs side-tab" style="left:-6px"><svg width="22" height="48" color="#fff"><svg x="6" y="17" width="9" height="14"><use href="#chev-l"/></svg></svg></div>
  <div class="abs side-tab" style="left:650px"><svg width="22" height="48" color="#fff"><svg x="7" y="17" width="9" height="14"><use href="#chev-r"/></svg></svg></div>
</section>

<section class="abs brands">
  <svg class="abs" style="left:12px;top:12px" width="12" height="18" color="#aaa"><use href="#chev-l"/></svg>
  <span class="brand-name" style="left:66px">Norvella</span>
  <span class="brand-name" style="left:192px">Quintaro</span>
  <span class="brand-name" style="left:311px">Lumeric Day</span>
  <span class="brand-name" style="left:440px">Saltfin</span>
  <span class="brand-name" style="left:536px">Arvexa</span>
  <svg class="abs" style="left:643px;top:12px" width="12" height="18" color="#aaa"><use href="#chev-r"/></svg>
</section>

<footer class="abs footer">
  <h4 style="left:110px">Contact Us</h4>
  <div class="f-icon" style="left:108px;top:47px"><svg width="21" height="21" viewBox="0 0 21 21"><path d="M7 5l2 3-1.5 1.5c.8 1.6 2 2.8 3.5 3.5L12.5 11.5l3 2-1 2.5C10 16 5 11 5 6z" fill="#fff"/></svg></div>
  <div class="f-text" style="left:140px;top:42px">+3(345) 48.61.702<br>+3(345) 48.61.702</div>
  <div class="f-icon" style="left:108px;top:86px"><svg width="21" height="21"><rect x="5" y="7" width="11" height="8" fill="#fff"/><path d="M5 7l5.5 4.5L16 7" fill="none" stroke="#f36f21"/></svg></div>
  <div class="f-text" style="left:140px;top:81px">store@kelvara.com<br>store@tamsil.com</div>
  <div class="f-icon" style="left:108px;top:124px"><svg width="21" height="21"><path d="M10.5 5L5 10h2v6h7v-6h2z" fill="#fff"/></svg></div>
  <div class="f-text" style="left:140px;top:120px">East 41st Marlow Street,<br>New York, 604812, U.S.A.</div>

  <h4 style="left:294px">Site Links</h4>
  <ul class="f-list" style="left:294px;top:42px"><li>Home</li><li>Create</li><li>About</li><li>Contact</li><li>Request a Quote</li></ul>

  <h4 style="left:455px">Shipping Info</h4>
  <ul class="f-list" style="left:455px;top:42px"><li>Site Map</li><li>Search Terms</li><li>Advanced Search</li><li>Mobile</li><li>Contact Us</li><li>Advanced Search</li></ul>

  <h4 style="left:618px">Newsletter</h4>
  <div class="abs news-input">Enter your email address</div>
  <div class="abs news-btn">Submit</div>
  <div class="badge" style="left:617px;top:84px;width:46px;height:26px"></div>
  <div class="badge" style="left:670px;top:84px;width:70px;height:26px;background:#555"></div>
  <div class="badge" style="left:745px;top:80px;width:31px;height:31px;border-radius:50%;background:#e8c24a"></div>
  <div class="badge" style="left:619px;top:131px;width:28px;height:16px"></div>
  <div class="badge" style="left:654px;top:131px;width:28px;height:16px;background:#3a8fd8"></div>
  <div class="badge" style="left:688px;top:131px;width:28px;height:16px"></div>
  <div class="badge" style="left:718px;top:131px;width:28px;height:16px;background:#2f76c4"></div>
  <div class="badge" style="left:750px;top:131px;width:28px;height:16px;background:#d9372a"></div>
  <div class="badge" style="left:782px;top:131px;width:28px;height:16px;background:#e6e6f2"></div>

  <div class="social" style="left:110px"><b></b>Chirp</div>
  <div class="social" style="left:152px"><b></b>Folkbook</div>
  <div class="social" style="left:208px"><b style="background:#f37a20"></b>RSS</div>
  <div class="abs copy">© 2013.www.brindlecove.com</div>
</footer>
</body>
</html>
```